Allied Health team of Physiotherapists & Occupational Therapists seek a business card design

We have our new logo, we now need our new business cards and stationary. Blossom: Lymphoedema & Women's Clinic is seeking a generic card design to represent our whole team and individual cards for each therapist that incorporates our new logo to communicate our holistic approach that is calming, nuturing, supportive and welcoming.
Our Physiotherapists and Occupational Therapists assess, treat and provide education for people who are at risk of or who have lymphoedema. This is often as a result of treatment for cancer. We provide pre-operative and post-operative management and cancer rehabilitation in our Pilates studio. Our team also consists of Physiotherapists who have a strong interest in pelvic floor and continence management for both men and women.

Target Market(s)

Mainly women health conscious

Industry/Entity Type

Allied Health: Physiotherapy / Occupational Therapy

Contact Information for Business Card

Address: 14 Calloway Ave Merriwood 3188 Phone: 84317560 fax: 8431 7564 Email: info@blossomcarepartners.com.au Website: blossomcarepartners.com.au Facebook address: facebook.com/BlossomLymphoedemaAndWomensCareCentre. Room to write appointments. Individual cards need to have name, office email and individual email and professional details

Requirements
Must have
• Logo as per uploaded documents

```html
<!DOCTYPE html>
<html lang="en">
<head>
<meta charset="utf-8">
<title>Blossom Business Cards</title>
<link href="https://fonts.googleapis.com/css2?family=Jost:wght@400;500;600&family=Lato:ital,wght@0,400;1,700&display=swap" rel="stylesheet">
<style>
  :root{
    --backdrop:#080808;
    --cream:#FFFBD8;
    --peach:#F8AE7E;
    --sage:#BFC8BA;
    --ink:#2E3236;
    --ink-soft:#3A3A3A;
    --light-text:#FFF6DE;
  }
  *{margin:0;padding:0;box-sizing:border-box}
  html,body{width:1200px;height:892px;overflow:hidden;background:var(--backdrop)}
  .stage{position:relative;width:1254px;height:932px;transform:scale(0.9569);transform-origin:0 0}
  .card{position:absolute;width:526px;height:301px;background:var(--cream);overflow:hidden;
        box-shadow:14px 16px 22px rgba(0,0,0,.55)}
  .card-front{left:233px;top:126px}
  .card-back{left:495px;top:505px}
  .card-shapes{position:absolute;inset:0;width:526px;height:301px}

  .name{position:absolute;right:19px;top:38px;font-family:"Lato",sans-serif;font-style:italic;font-weight:700;
        font-size:27px;color:var(--ink);letter-spacing:.2px}
  .role{position:absolute;right:20px;top:75px;font-family:"Jost",sans-serif;font-size:13px;color:var(--ink)}
  .brand{position:absolute;left:370px;top:194px;display:flex;align-items:center;gap:8px}
  .brand-dot{width:12px;height:12px;border-radius:50%;background:var(--light-text)}
  .brand-name{font-family:"Jost",sans-serif;font-weight:500;font-size:26px;color:var(--light-text)}
  .services{position:absolute;left:19px;top:234px;font-family:"Jost",sans-serif;font-weight:600;font-size:13.5px;
            line-height:17px;color:var(--ink-soft)}

  .contacts{position:absolute;left:48px;top:62px;list-style:none;font-family:"Jost",sans-serif;color:var(--light-text)}
  .contacts li{display:flex;align-items:center;gap:5px;height:20.7px;font-size:13.5px}
  .contacts .num{font-size:15px;letter-spacing:1.5px}
  .icon{width:15px;height:15px;flex:none}
  .appointment{position:absolute;left:48px;top:195px;font-family:"Jost",sans-serif;font-size:15.5px;color:var(--light-text)}
  .appointment .dots{letter-spacing:1px;font-size:13px}
  .website{position:absolute;left:28px;top:245px;display:flex;align-items:center;gap:6px;font-family:"Jost",sans-serif;
           font-size:15.5px;color:var(--light-text)}
</style>
</head>
<body>
<main class="stage">
  <section class="card card-front" aria-label="Business card front">
    <svg class="card-shapes" viewBox="0 0 526 301" aria-hidden="true">
      <path d="M257 0 H290 L330 284 H316 Q308 284 306 276 Z" fill="var(--sage)"/>
      <path d="M277 0 H526 V301 H344 Q332 301 330 289 Z" fill="var(--peach)"/>
    </svg>
    <h1 class="name">Maren Holt</h1>
    <p class="role">Physiotherapist</p>
    <div class="brand"><span class="brand-dot"></span><span class="brand-name">Blossom</span></div>
    <p class="services">Lymphoedema &amp; Oncology Rehabilitation<br>Continence &amp; Pelvic Floor</p>
  </section>

  <section class="card card-back" aria-label="Business card back">
    <svg class="card-shapes" viewBox="0 0 526 301" aria-hidden="true">
      <path d="M348 18 Q358 18 360 28 L408 301 H388 Z" fill="var(--sage)"/>
      <path d="M0 0 H325 Q336 0 338 12 L388 301 H0 Z" fill="var(--peach)"/>
    </svg>
    <ul class="contacts">
      <li><svg class="icon" viewBox="0 0 16 16"><circle cx="8" cy="8" r="7" fill="none" stroke="currentColor" stroke-width="1.3"/><path d="M5.2 4.3l1.3-.3.8 1.8-.9.7c.5 1 1.2 1.8 2.2 2.3l.7-.9 1.8.8-.3 1.3c-3 .2-5.8-2.6-5.6-5.7z" fill="currentColor"/></svg><span class="num">8431 7560</span></li>
      <li><svg class="icon" viewBox="0 0 16 16"><circle cx="8" cy="8" r="7" fill="none" stroke="currentColor" stroke-width="1.3"/><rect x="4.5" y="6" width="7" height="5" rx=".8" fill="currentColor"/><rect x="6" y="4" width="4" height="2.5" fill="none" stroke="currentColor"/></svg><span class="num">8431 7564</span></li>
      <li><svg class="icon" viewBox="0 0 16 16"><circle cx="8" cy="8" r="7" fill="currentColor"/><rect x="4.3" y="5.3" width="7.4" height="5.4" rx=".6" fill="var(--peach)"/><path d="M4.6 5.8L8 8.3l3.4-2.5" fill="none" stroke="currentColor" stroke-width=".9"/></svg><span>info@blossomcarepartners.com.au</span></li>
      <li><svg class="icon" viewBox="0 0 16 16"><circle cx="8" cy="8" r="7" fill="none" stroke="currentColor" stroke-width="1.3"/><path d="M8 12.5s-3-3.2-3-5.5a3 3 0 016 0c0 2.3-3 5.5-3 5.5z" fill="currentColor"/><circle cx="8" cy="7" r="1.1" fill="var(--peach)"/></svg><span>14 Calloway Ave, Merriwood 3188</span></li>
    </ul>
    <p class="appointment">Next Appointment <span class="dots">.........................</span></p>
    <p class="website"><svg class="icon" viewBox="0 0 16 16"><circle cx="8" cy="8" r="7" fill="none" stroke="currentColor" stroke-width="1.2"/><ellipse cx="8" cy="8" rx="3" ry="7" fill="none" stroke="currentColor" stroke-width=".9"/><path d="M1 8h14M2.5 4.5h11M2.5 11.5h11" stroke="currentColor" stroke-width=".9"/></svg><span>blossomcarepartners.com.au (Book Online)</span></p>
  </section>
</main>
</body>
</html>
```